New Wordpress Design Project

The website is my name tessamarlowgrant.com

I need a website design that will be graphically pleasing and have a crisp feel to it. I am a business and personal coach and have many different niches that I work with. I am looking for the central site to describe who I am and how I help people - I help people "wake up" to make conscious choices in their lives. I use hypnosis but do not want it to be esoteric, I ground the hypnosis and base it in science of how people can manage their state to reach their full potential in their lives and in business. I work one on one but also do public speaking and recently started to do trainings with corporations, helping people improve their business. I am looking at this as a merge of hypnosis and other tools with the business or corporate world - based in science - neuroplasticity, brain training etc. I will be helping people to overcome anxiety and stress, limiting beliefs, controlling and choosing habits that will work for them, fears and phobias, golf/sports improvement, weight loss.

Really helping people to center back with themselves, to not be so caught up in their head but drop into their heart and with what is really going on. My mission is to connect them back with themselves, using language, state and conscious choice.

I work online with entrepreneurs helping them to get unstuck, move past fears and limiting beliefs to create the business of their dreams.

I added a file of what I am envisioning on the right hand side of my site to show people the different niches I am involved with.

Some sites that I like www.brindaquell.com www.corabethwynn.org http://www.devoratusk.com/ , Details for my new Wordpress Design Project will be added soon. , The website is my name tessamarlowgrant.com

the square boxes graphic below is similar to one that I will be making for a page on my site for clarity and crispness. But will be creating it more in the teal color.

Target Market(s)

My target market are both male and female 30-50 either entreprenuers/business people

Industry/Entity Type

Training

Requirements
Must have
• A video with an opt in box
My background color is teal/blue (see below file)
Social media links

```html
<!DOCTYPE html>
<html lang="en">
<head>
<meta charset="utf-8">
<title>Tessa Marlow Grant – Coaching</title>
<link rel="stylesheet" href="https://fonts.googleapis.com/css2?family=Open+Sans:wght@400;600;700&family=Oswald:wght@500;600&display=swap">
<style>
:root{
  --teal:#1fcfb4;
  --teal-dark:#0f6f66;
  --lime:#8ec63f;
  --orange:#f47b20;
  --blue:#1f6aa5;
  --ink:#333;
  --muted:#555;
  --grey-bg:#ececec;
  --footer:#242424;
  --white:#fff;
}
*{margin:0;padding:0;box-sizing:border-box}
html,body{width:1200px;height:2356px;overflow:hidden}
body{position:relative;background:var(--white);font-family:"Open Sans",sans-serif;color:var(--ink)}
h1,h2,h3{font-weight:400}
.abs{position:absolute}

/* header */
.site-header{position:absolute;left:0;top:0;width:1200px;height:153px;background:var(--white);border-top:4px solid var(--teal);border-bottom:2px solid #dcdcdc}
.phone-tab{left:732px;top:0;width:297px;height:36px;background:var(--teal);border-radius:0 0 18px 18px;color:var(--white);font-size:25px;display:flex;align-items:center;justify-content:center;gap:12px}
.brand{left:170px;top:46px;display:flex;align-items:center;gap:12px}
.brand-mark{width:54px;height:54px;border-radius:50%;background:var(--orange)}
.brand-name{font-size:33px;font-weight:700;color:#e9b10c}
.social{left:913px;top:56px;display:flex;gap:8px}
.social span{width:24px;height:24px;border-radius:50%;background:var(--teal)}
.main-nav{left:619px;top:109px;display:flex;height:44px}
.main-nav a{font-size:12px;color:#555;text-decoration:none;padding:0 17px;display:flex;align-items:center;text-transform:uppercase}
.main-nav a.active{background:var(--teal);color:var(--white);padding:0 17px;width:66px;justify-content:center}

/* hero */
.hero{left:0;top:155px;width:1200px;height:372px;background:radial-gradient(circle at 80% 30%,#4a2a48 0,#2a1522 30%,#120a0c 70%),#180d10}
.hero-photo{left:269px;top:178px;width:322px;height:322px;border-radius:50%;background:radial-gradient(circle at 50% 40%,#e8cfa8,#c9a070 60%,#c23d9a 95%);border:6px solid var(--white)}
.hero-title{left:711px;top:218px;width:283px;text-align:center;font-family:"Oswald",sans-serif;font-weight:600;font-size:40px;color:var(--lime)}
.hero-rule{left:694px;top:284px;width:306px;height:1px;background:#6b5a60}
.hero-text{left:694px;top:311px;width:306px;text-align:center;color:#f1f1f1;font-size:19px;line-height:26.5px}
.hero-btn{left:767px;top:426px;width:160px;height:43px;background:var(--orange);color:var(--white);font-family:"Oswald",sans-serif;font-weight:500;font-size:20px;display:flex;align-items:center;justify-content:center}
.hero-line{left:0;top:527px;width:1200px;height:5px;background:var(--lime)}

/* intro */
.intro-photo{left:178px;top:565px;width:190px;height:190px;border-radius:50%;background:radial-gradient(circle at 50% 35%,#f0d8b0,#d9b27a 50%,#4f7a49 85%)}
.intro-title{left:418px;top:574px;font-size:29px;color:var(--blue);letter-spacing:.3px}
.intro-rule{left:418px;top:612px;width:190px;height:2px;background:#bbb}
.intro-text{left:418px;top:626px;width:617px;font-size:12px;line-height:18.5px;color:var(--muted);text-align:justify}
.read-more{font-size:12px;color:var(--ink)}
.intro-more{left:418px;top:728px}

/* services */
.services{left:0;top:797px;width:1200px;height:503px;background:var(--grey-bg)}
.card{position:absolute;top:851px;width:275px;height:405px;background:var(--white);border-bottom:3px solid var(--teal)}
.card-photo{width:275px;height:181px}
.card-title{position:absolute;top:214px;left:0;width:100%;text-align:center;font-size:19px;color:#444;text-transform:uppercase}
.card-title b{font-weight:400;color:var(--teal)}
.card-title::after{content:"";display:block;width:180px;height:2px;background:#999;margin:5px auto 0}
.card-text{position:absolute;top:268px;left:22px;width:231px;font-size:12px;line-height:20px;color:var(--muted);text-align:justify}
.card-more{position:absolute;top:356px;left:0;width:100%;text-align:center}

/* blog */
.blog-title{left:0;top:1352px;width:1200px;text-align:center;font-size:25px;color:var(--orange)}
.blog-rule{left:533px;top:1396px;width:130px;height:3px;background:var(--orange)}
.post{position:absolute;top:1457px;width:280px;height:110px}
.post-date{position:absolute;left:0;top:0;width:74px;height:61px;background:#e5e5e5;border-bottom:5px solid #444;font-size:17px;line-height:21px;color:#444;padding:10px 0 0 9px}
.post-title{position:absolute;left:90px;top:0;width:195px;font-size:16px;line-height:22px;color:var(--orange);white-space:nowrap;letter-spacing:-.2px}
.post-text{position:absolute;left:90px;top:58px;width:185px;font-size:11.5px;line-height:16px;color:var(--muted);text-align:justify}
.pager{top:1585px;display:flex;gap:2px}
.pager span{width:25px;height:25px;display:flex;align-items:center;justify-content:center}
.pager .prev{background:#e2e2e2}
.pager .next{background:#1fa0e8}

/* video + opt-in */
.media-band{left:0;top:1676px;width:1200px;height:403px;background:linear-gradient(90deg,#2aa88f,#4bbca0 30%,#2f9e88 60%,#3eb39c)}
.video{left:166px;top:1733px;width:499px;height:282px;background:#111}
.video-bar{position:absolute;left:0;top:0;width:100%;height:28px;background:#1a1a1a;color:#ddd;font-size:12px;padding:6px 10px;display:flex;justify-content:space-between}
.video-frame{position:absolute;left:0;top:28px;width:100%;height:224px;background:radial-gradient(circle at 55% 55%,#e7d8b0,#a7b87a 55%,#5d6e3d)}
.play{position:absolute;left:225px;top:118px;width:50px;height:36px;border-radius:8px;background:rgba(20,20,20,.85);display:flex;align-items:center;justify-content:center}
.video-controls{position:absolute;left:0;bottom:0;width:100%;height:30px;background:#1c1c1c;color:#bbb;font-size:10px;display:flex;align-items:center;gap:14px;padding:0 12px}
.optin-visual{left:797px;top:1721px;width:180px;height:180px;border-radius:50%;background:radial-gradient(circle at 50% 55%,#d98a2a 0,#8a5a22 30%,#0f3d37 60%)}
.optin{left:736px;top:1873px;width:298px;height:143px;background:#0f3d37;padding:12px 22px}
.optin p{font-size:11px;line-height:14px;color:#7ee8d4;font-weight:600;text-align:justify}
.email{position:absolute;left:23px;top:54px;width:250px;height:33px;background:#0b0b0b;color:var(--white);font-size:12px;padding:8px 13px}
.submit{position:absolute;left:79px;top:97px;width:141px;height:33px;background:#17806f;color:var(--white);font-size:12px;display:flex;align-items:center;justify-content:center}

/* footer */
.site-footer{left:0;top:2079px;width:1200px;height:277px;background:var(--footer);border-top:3px solid var(--teal)}
.f-col{position:absolute;top:2120px;color:#ccc;font-size:10.5px}
.f-head{font-size:12px;color:var(--lime);text-transform:uppercase;margin-bottom:14px}
.quick li{list-style:none;line-height:22px;padding-left:12px;position:relative}
.quick li::before{content:"";position:absolute;left:0;top:10px;width:3px;height:3px;background:#ccc;border-radius:50%}
.copy{margin-top:2px}
.testi{display:flex;gap:10px;margin-bottom:16px}
.avatar{width:42px;height:42px;border-radius:50%;background:radial-gradient(circle at 50% 40%,#e8d0b0,#a57b55);border:2px solid var(--white);flex:none}
.q{width:190px;line-height:15px}
.by{font-style:italic;margin-top:6px;font-size:10px}
.tweet{width:240px;line-height:15px;margin-bottom:16px}
.view-more{color:var(--white);text-decoration:underline;font-size:11px}
</style>
</head>
<body>

<header class="site-header">
  <div class="abs phone-tab">
    <svg width="18" height="18" viewBox="0 0 24 24" aria-hidden="true"><path fill="#fff" d="M6.6 10.8a15 15 0 0 0 6.6 6.6l2.2-2.2c.3-.3.7-.4 1-.2 1.1.4 2.3.6 3.6.6.6 0 1 .4 1 1V20c0 .6-.4 1-1 1A17 17 0 0 1 3 4c0-.6.4-1 1-1h3.5c.6 0 1 .4 1 1 0 1.3.2 2.5.6 3.6.1.3 0 .7-.2 1z"/></svg>
    1234 5678 901
  </div>
  <div class="abs brand"><span class="brand-mark"></span><span class="brand-name">TessaMarlowGrant.com</span></div>
  <div class="abs social" aria-label="Social media links"><span></span><span></span><span></span><span></span></div>
  <nav class="abs main-nav">
    <a class="active" href="#">Home</a><a href="#">My Story</a><a href="#">Coaching</a><a href="#">Testimonials</a><a href="#">Contact</a>
  </nav>
</header>

<section>
  <div class="abs hero" role="img" aria-label="Dark background with soft coloured bokeh lights"></div>
  <div class="abs hero-photo" role="img" aria-label="Portrait of the coach smiling, in a pink top"></div>
  <h1 class="abs hero-title">LOREMIPSUMDOLOR</h1>
  <div class="abs hero-rule"></div>
  <p class="abs hero-text">Lorem Ipsum has been<br>the industry's standard dummy<br>text ever since</p>
  <a class="abs hero-btn">LOREMIPSUM</a>
  <div class="abs hero-line"></div>
</section>

<section>
  <div class="abs intro-photo" role="img" aria-label="Portrait of the coach outdoors"></div>
  <h2 class="abs intro-title">MEET TESSA AND CONNECT!</h2>
  <div class="abs intro-rule"></div>
  <p class="abs intro-text">Lorem Ipsum is simply dummy text of the printing and typesetting industry. Lorem Ipsum has been the industry's standard dummy text ever since the 1500s, when an unknown printer took a galley of type and scrambled it to make a type specimen book. It has survived not only five centuries, but also the leap into electronic typesetting, remaining essentially unchanged</p>
  <span class="abs read-more intro-more">[ read more ]</span>
</section>

<section class="abs services"></section>
<article class="card" style="left:166px">
  <div class="card-photo" role="img" aria-label="Coach presenting to a seated group" style="background:linear-gradient(135deg,#7a4a36,#c89a80 45%,#3d4a2e)"></div>
  <h3 class="card-title"><b>Coaching</b> Sessions</h3>
  <p class="card-text">Lorem Ipsum is simply dummy text of the printing and typesetting industry. Lorem Ipsum has been the industry's</p>
  <span class="card-more read-more">[ read more ]</span>
</article>
<article class="card" style="left:459px">
  <div class="card-photo" role="img" aria-label="Silhouette of a cyclist pushing a bike uphill at sunset" style="background:radial-gradient(circle at 50% 40%,#ffd070,#f29a1a 55%,#c05a06)"></div>
  <h3 class="card-title"><b>Your</b> Passion</h3>
  <p class="card-text">Lorem Ipsum is simply dummy text of the printing and typesetting industry. Lorem Ipsum has been the industry's</p>
  <span class="card-more read-more">[ read more ]</span>
</article>
<article class="card" style="left:759px">
  <div class="card-photo" role="img" aria-label="Business people standing on white blocks" style="background:linear-gradient(180deg,#f6f6f6,#d8d8d8)"></div>
  <h3 class="card-title"><b>Help</b> You Success</h3>
  <p class="card-text">Lorem Ipsum is simply dummy text of the printing and typesetting industry. Lorem Ipsum has been the industry's</p>
  <span class="card-more read-more">[ read more ]</span>
</article>

<section>
  <h2 class="abs blog-title">BLOG</h2>
  <div class="abs blog-rule"></div>
  <article class="post" style="left:166px">
    <div class="post-date">12 Jan<br>2014</div>
    <h3 class="post-title">Lorem Ipsum has been<br>the industry's text</h3>
    <p class="post-text">Lorem Ipsum is simply dummy text of the printing and typesetting industry.</p>
  </article>
  <article class="post" style="left:459px">
    <div class="post-date">12 Jan<br>2014</div>
    <h3 class="post-title">Lorem Ipsum has been<br>the industry's text</h3>
    <p class="post-text">Lorem Ipsum is simply dummy text of the printing and typesetting industry.</p>
  </article>
  <article class="post" style="left:763px">
    <div class="post-date">12 Jan<br>2014</div>
    <h3 class="post-title">Lorem Ipsum has been<br>the industry's text</h3>
    <p class="post-text">Lorem Ipsum is simply dummy text of the printing and typesetting industry.</p>
  </article>
  <div class="abs pager" style="left:984px">
    <span class="prev"><svg width="10" height="12" viewBox="0 0 10 12"><path d="M7 1 2 6l5 5" stroke="#aaa" stroke-width="2" fill="none"/></svg></span>
    <span class="next"><svg width="10" height="12" viewBox="0 0 10 12"><path d="M3 1l5 5-5 5" stroke="#fff" stroke-width="2" fill="none"/></svg></span>
  </div>
</section>

<section>
  <div class="abs media-band" role="img" aria-label="Teal-tinted collage of portraits of the coach outdoors"></div>
  <div class="abs video">
    <div class="video-bar"><span>www.tessamarlowgrant.com</span><span>⋯</span></div>
    <div class="video-frame" role="img" aria-label="Video still of the coach speaking beside red roses"></div>
    <div class="play"><svg width="16" height="18" viewBox="0 0 16 18"><path d="M2 1l13 8-13 8z" fill="#fff"/></svg></div>
    <div class="video-controls">
      <svg width="12" height="12" viewBox="0 0 12 12"><path d="M2 1l9 5-9 5z" fill="#bbb"/></svg>
      <span>0:00 / 0:55</span>
    </div>
  </div>
  <div class="abs optin-visual" role="img" aria-label="Book and disc product set"></div>
  <form class="abs optin">
    <p>Lorem Ipsum is simply dummy text Lorem Ipsum is simply dummy text of the...</p>
    <div class="email">Email Address</div>
    <div class="submit">SUBMIT</div>
  </form>
</section>

<footer class="abs site-footer"></footer>
<div class="f-col" style="left:165px">
  <div class="f-head">Quick Links</div>
  <ul class="quick"><li>Home</li><li>My Story</li><li>Coaching</li><li>Testimonials</li><li>FAQs</li><li>Contact</li></ul>
  <div class="copy">Copyright © 2014. All right reserved.</div>
</div>
<div class="f-col" style="left:435px">
  <div class="f-head">Testimonial</div>
  <div class="testi"><div class="avatar" role="img" aria-label="Client portrait"></div><div class="q">Lorem Ipsum has been the industry's standard dummy text<div class="by">- Johd Dsot</div></div></div>
  <div class="testi"><div class="avatar" role="img" aria-label="Client portrait"></div><div class="q">Lorem Ipsum has been the industry's standard dummy text<div class="by">- Johd Dsot</div></div></div>
  <a class="view-more">View More</a>
</div>
<div class="f-col" style="left:762px">
  <div class="f-head">Twitter</div>
  <div class="tweet">Lorem Ipsum has been the industry's standard dummy text<div class="by">- Johd Dsot &nbsp;&nbsp;&nbsp; 15 Dec 2013</div></div>
  <div class="tweet">Lorem Ipsum has been the industry's standard dummy text<div class="by">- Johd Dsot &nbsp;&nbsp;&nbsp; 15 Dec 2013</div></div>
  <a class="view-more">View More</a>
</div>

</body>
</html>
```